Criação de Papelaria para Brisa & Aurora
" Clinica Multidiciplinar com equipamentos de alta tecnologia para tratamentos esteticos faciais e corporais "

```html
<!DOCTYPE html>
<html lang="pt-BR">
<head>
<meta charset="utf-8">
<title>Brisa &amp; Aurora – Envelope</title>
<link rel="stylesheet" href="https://fonts.googleapis.com/css2?family=Josefin+Sans:wght@300&family=Lato:wght@400&display=swap">
<style>
  :root {
    --backdrop: #565658;
    --paper: #e9e9e9;
    --paper-light: #f4f4f4;
    --paper-shade: #d9d9d9;
    --liner-dark: #3c3c3e;
    --liner-mid: #58585a;
    --ink: #6a6a6c;
    --ink-soft: #8a8a8c;
  }
  * { box-sizing: border-box; margin: 0; padding: 0; }
  html, body { width: 1200px; height: 1200px; overflow: hidden; }
  body { background: var(--backdrop); position: relative; font-family: "Lato", sans-serif; }

  .envelope { position: absolute; left: 150px; width: 900px; }

  .envelope-front {
    top: 100px; height: 420px;
    background: linear-gradient(135deg, var(--paper-light), var(--paper) 55%, var(--paper-shade));
  }
  .surface-texture {
    position: absolute; inset: 0;
    background: linear-gradient(160deg, rgba(255,255,255,0.35), rgba(200,200,200,0.15) 60%, rgba(255,255,255,0.25));
  }
  .brand-name {
    position: absolute;
    font-family: "Josefin Sans", sans-serif;
    font-weight: 300;
    color: var(--ink);
    letter-spacing: 0.12em;
    text-transform: uppercase;
    white-space: nowrap;
  }
  .envelope-front .brand-name { left: 60px; top: 56px; font-size: 38px; }

  .envelope-back {
    top: 740px; height: 400px;
    background: linear-gradient(135deg, var(--paper-light), var(--paper) 50%, var(--paper-shade));
  }
  .flap { position: absolute; left: 150px; top: 600px; width: 900px; height: 141px; display: block; }

  .envelope-back .brand-name { right: 60px; top: 150px; font-size: 30px; }
  .contact-block {
    position: absolute; right: 60px; top: 200px;
    text-align: right; font-size: 13px; line-height: 1.7; color: var(--ink-soft);
  }
  .address-block {
    position: absolute; left: 60px; bottom: 50px;
    font-size: 13px; line-height: 1.7; color: var(--ink-soft);
  }
  .website {
    position: absolute; right: 60px; bottom: 50px;
    font-size: 13px; color: var(--ink-soft);
  }
</style>
</head>
<body>

  <section class="envelope envelope-front">
    <div class="surface-texture" role="img" aria-label="Padrão decorativo de ondas em relevo sobre o papel"></div>
    <span class="brand-name">Brisa &amp; Aurora</span>
  </section>

  <svg class="flap" viewBox="0 0 900 141" role="img" aria-label="Aba aberta com forro interno estampado em padrão de ondas">
    <defs>
      <linearGradient id="liner" x1="0" y1="0" x2="1" y2="1">
        <stop offset="0" stop-color="#5c5c5e"/>
        <stop offset="1" stop-color="#3c3c3e"/>
      </linearGradient>
    </defs>
    <path d="M0 141 L60 10 Q64 0 76 0 L824 0 Q836 0 840 10 L900 141 Z" fill="url(#liner)"/>
  </svg>

  <section class="envelope envelope-back">
    <div class="surface-texture" role="img" aria-label="Padrão decorativo de ondas em relevo sobre o papel"></div>
    <span class="brand-name">Brisa &amp; Aurora</span>
    <p class="contact-block">
      21 3200-4100 &nbsp;|&nbsp; 21 99000-8100<br>
      contato@brisaaurora.com.br
    </p>
    <p class="address-block">
      Rua das Acácias, 210<br>
      Sala 302 – Centro<br>
      Rio de Janeiro – 20000-000
    </p>
    <p class="website">www.brisaaurora.com.br</p>
  </section>

</body>
</html>
```